Business Card Design Project

TRX Solutions is a Electrical and Communications Services and Maintenance contractor to the Mining Oil and Gas sectors of Australia.
Our clients will be planners, Schedulers, Tradespeople and Engineers

We are yet to determine the primary colours that we will use on the business cards but the logos attached will form foundation of the colours used for logos on Business cards, Website, Uniforms, vehicles etc.

Target Market(s)

Mining engineers and shedulers

Industry/Entity Type

Contractor

Requirements
Must have
• information to be included on the card

Name: Derek Hanley
Title: Managing Director
Company: TRX Solutions Pty Ltd
Phone: 08 9XXX XXXX
Mobile 0400 318 942
email: dhanley@trxsolutionsgroup.com.au
Website www.trxsolutionsgroup.com.au

Address: U5/14 Kettering Street Malaga, WA 6090
Postal Address: PO Box 7183 Malaga WA 6944

Nice to have
• Double sided. Maybe the logo on the back

```html
<!DOCTYPE html>
<html lang="en">
<head>
<meta charset="utf-8">
<title>TRX Solutions – Business Card</title>
<link rel="stylesheet" href="https://fonts.googleapis.com/css2?family=Michroma&display=swap">
<style>
  :root {
    --navy: #16284a;
    --navy-light: #22396a;
    --navy-dark: #0c1830;
    --orange: #f0801e;
    --white: #ffffff;
    --paper: #f6f7f8;
    --paper-shade: #e3e6ea;
    --muted: #5a6680;
    --backdrop: #e9eaec;
    --backdrop-light: #f8f8f9;
  }
  * { box-sizing: border-box; margin: 0; padding: 0; }
  html, body { width: 1200px; height: 900px; overflow: hidden; }
  body {
    background: radial-gradient(ellipse at 50% 45%, var(--backdrop-light) 0%, var(--backdrop) 100%);
    font-family: "Michroma", "Arial", sans-serif;
    position: relative;
  }
  .card {
    position: absolute;
    width: 540px;
    height: 310px;
    box-shadow: 0 8px 22px rgba(0,0,0,0.22);
    overflow: hidden;
  }

  /* Front: name side */
  .card--front {
    left: 80px;
    top: 110px;
    background: radial-gradient(ellipse at 50% 50%, var(--navy-light) 0%, var(--navy) 55%, var(--navy-dark) 100%);
    display: flex;
    align-items: center;
    justify-content: center;
  }
  .brand-name {
    color: var(--white);
    font-size: 30px;
    font-weight: 400;
    letter-spacing: 1px;
  }

  /* Back: details side */
  .card--back {
    left: 580px;
    top: 470px;
    background: linear-gradient(160deg, var(--white) 0%, var(--paper) 55%, var(--paper-shade) 100%);
  }
  .company-band {
    height: 46px;
    background: var(--navy);
    color: var(--white);
    font-size: 18px;
    padding: 12px 20px 0;
    letter-spacing: 0.5px;
  }
  .person {
    position: absolute;
    left: 150px;
    top: 96px;
    text-align: right;
  }
  .person__name {
    color: var(--navy);
    font-size: 32px;
    font-weight: 400;
    -webkit-text-stroke: 1px var(--navy);
    letter-spacing: 0.5px;
  }
  .person__title {
    color: var(--navy);
    font-size: 10px;
    margin-top: 6px;
    margin-right: 14px;
  }
  .addresses {
    position: absolute;
    left: 20px;
    top: 178px;
    color: var(--muted);
    font-size: 8px;
    font-style: normal;
    line-height: 1.6;
  }
  .contact-band {
    position: absolute;
    left: 0;
    bottom: 0;
    width: 100%;
    height: 86px;
    background: var(--navy);
    border-top: 5px solid var(--orange);
    padding: 16px 16px 0 20px;
    display: flex;
    justify-content: space-between;
    color: var(--white);
  }
  .contact-list { list-style: none; }
  .contact-list li {
    display: flex;
    align-items: center;
    gap: 7px;
    font-size: 11px;
    line-height: 1;
    margin-bottom: 13px;
  }
  .contact-list--online li { font-size: 9px; }
  .contact-list--online { padding-top: 14px; }
  .icon { width: 12px; height: 12px; flex: none; }
</style>
</head>
<body>

<section class="card card--front" aria-label="Business card front">
  <p class="brand-name">TRX Solutions</p>
</section>

<section class="card card--back" aria-label="Business card back">
  <header class="company-band">TRX Solutions Pty Ltd</header>

  <div class="person">
    <h1 class="person__name">Derek Hanley</h1>
    <p class="person__title">Managing Director</p>
  </div>

  <address class="addresses">
    U5/14 Kettering Street Malaga, WA 6090<br>
    PO Box 7183 Malaga WA 6944
  </address>

  <footer class="contact-band">
    <ul class="contact-list contact-list--phone">
      <li>
        <svg class="icon" viewBox="0 0 12 12" aria-hidden="true"><path d="M2.5 1 L4.5 1 L5 3.5 L3.8 4.4 Q4.8 6.8 7.6 8.2 L8.5 7 L11 7.5 L11 9.5 Q10.5 11 9 11 Q2 9.8 1 3 Q1 1.5 2.5 1Z" fill="#ffffff"/></svg>
        <span>08 9XXX XXXX</span>
      </li>
      <li>
        <svg class="icon" viewBox="0 0 12 12" aria-hidden="true"><rect x="3" y="0.5" width="6" height="11" rx="1" fill="#ffffff"/><rect x="4" y="2" width="4" height="6" fill="#16284a"/><circle cx="6" cy="9.8" r="0.7" fill="#16284a"/></svg>
        <span>0400 318 942</span>
      </li>
    </ul>
    <ul class="contact-list contact-list--online">
      <li>
        <svg class="icon" viewBox="0 0 12 12" aria-hidden="true"><rect x="0.5" y="2" width="11" height="8" fill="#ffffff"/><path d="M0.8 2.4 L6 6.6 L11.2 2.4" fill="none" stroke="#16284a" stroke-width="1"/></svg>
        <span>dhanley@trxsolutionsgroup.com.au</span>
      </li>
      <li>
        <svg class="icon" viewBox="0 0 12 12" aria-hidden="true"><circle cx="6" cy="6" r="5.5" fill="#ffffff"/><ellipse cx="6" cy="6" rx="2.2" ry="5.5" fill="none" stroke="#16284a" stroke-width="0.8"/><path d="M0.5 6 H11.5 M1.5 3.2 H10.5 M1.5 8.8 H10.5" stroke="#16284a" stroke-width="0.8"/></svg>
        <span>www.trxsolutionsgroup.com.au</span>
      </li>
    </ul>
  </footer>
</section>

</body>
</html>
```